Business Cards for a Junk Removal Company

Hello,
We are looking to have business cards designed that are simple, bold, easy to read, and right to the point. Please see the attachments for our logo files. We want the card to be yellow on both sides ( Color code Yellow: #FFE01B). The logo text font is (Rockstar Extra Bold) and this is also in the files attached. Please make the text black for the logo. On the back side of the card, you can use white and black for text. Thank you in advance for your hard work!

Front of card-
Harbor Haul Away (logo)
Back of card-
Harbor Haul Away
Donate - Recycle - Dispose
555-271-8093
www.harborhaulaway.example
info@harborhaulaway.example

Industry/Entity Type

Junk removal

Contact Information for Business Card

FRONT OF CARD- Harbor Haul Away (logo) BACK OF CARD- Harbor Haul Away Donate - Recycle - Dispose 555-271-8093 www.harborhaulaway.example info@harborhaulaway.example

Font styles to use
Other font styles liked:
• Rockstar Extra Bold

Colors
FFF300
FFF600
FEFA6F
FFFEC7
FFFEE8

Requirements
Must have
• Must have color code Yellow: #FFE01B for the background of front and back of the card

```html
<!DOCTYPE html>
<html lang="en">
<head>
<meta charset="utf-8">
<title>Harbor Haul Away – Business Cards</title>
<link rel="stylesheet" href="https://fonts.googleapis.com/css2?family=Anton&family=Arimo:wght@400&display=swap">
<style>
  :root {
    --stage: #dedede;
    --card-yellow: #f0d444;
    --pattern-yellow: #dcc03a;
    --pattern-yellow-soft: #e4c93f;
    --ink: #111111;
  }
  * { box-sizing: border-box; margin: 0; padding: 0; }
  html, body {
    width: 1200px;
    height: 801px;
    overflow: hidden;
    background: var(--stage);
  }
  .sheet {
    position: relative;
    width: 1200px;
    height: 801px;
  }
  .card {
    position: absolute;
    top: 252px;
    width: 520px;
    height: 297px;
    background: var(--card-yellow);
    overflow: hidden;
  }
  .card--info { left: 60px; }
  .card--brand { left: 620px; }

  .info-block {
    position: absolute;
    inset: 0;
    display: flex;
    flex-direction: column;
    align-items: center;
    justify-content: center;
    text-align: center;
    color: var(--ink);
  }
  .company-name {
    font-family: "Anton", "Arial Narrow", sans-serif;
    font-size: 30px;
    letter-spacing: 0.5px;
    text-transform: uppercase;
    line-height: 1.05;
  }
  .tagline {
    font-family: "Arimo", Arial, sans-serif;
    font-size: 17px;
    margin-top: 2px;
  }
  .divider {
    width: 96px;
    height: 1.5px;
    background: var(--ink);
    margin: 20px 0 22px;
  }
  .contact-line {
    font-family: "Arimo", Arial, sans-serif;
    font-size: 17px;
    line-height: 1.5;
  }
  .contact-line--phone { margin-bottom: 14px; }

  .brand-pattern {
    position: absolute;
    inset: 0;
    background: repeating-linear-gradient(
      0deg,
      var(--pattern-yellow-soft) 0 18px,
      var(--pattern-yellow) 18px 36px
    );
  }
  .brand-mark {
    position: absolute;
    right: 34px;
    bottom: 64px;
    display: flex;
    align-items: center;
    gap: 8px;
    background: var(--card-yellow);
    padding: 6px 10px;
  }
  .brand-mark__square {
    width: 16px;
    height: 16px;
    background: var(--ink);
  }
  .brand-mark__name {
    font-family: "Anton", "Arial Narrow", sans-serif;
    font-size: 24px;
    color: var(--ink);
    text-transform: uppercase;
    line-height: 1;
  }
</style>
</head>
<body>
  <main class="sheet">
    <section class="card card--info" aria-label="Card front with contact details">
      <div class="info-block">
        <h1 class="company-name">Harbor Haul Away</h1>
        <p class="tagline">Donate - Recycle - Dispose</p>
        <div class="divider"></div>
        <p class="contact-line contact-line--phone">555-271-8093</p>
        <p class="contact-line">www.harborhaulaway.example</p>
        <p class="contact-line">info@harborhaulaway.example</p>
      </div>
    </section>

    <section class="card card--brand" aria-label="Card back with brand name">
      <div class="brand-pattern" role="img" aria-label="Tone-on-tone repeating brand name pattern"></div>
      <div class="brand-mark">
        <span class="brand-mark__square"></span>
        <span class="brand-mark__name">Harbor Haul Away</span>
      </div>
    </section>
  </main>
</body>
</html>
```